Building sign design

We need a sign design for the front of our automotive workshop building. The sign needs to fit the colours of our building and company. (black, red, grey and white). The sign needs to stand out and be a modern.

Sign is to replace the red Corvane Cells sign. 2900mmx2900mm.
Company logo attached (Fastlane).
Also photos of old sign and building.

Sign needs to feature Fastlane logo at top and what we do below.

-Warrant of Fitness
-Vehicle Servicing
-All Mechanical Repairs
-Tyres & Wheel Alignments
-Batteries & Diagnostics
-Automotive Parts
-Vehicle Sales.

Also needs a large "WOF" somewhere on sign.

And contact details at bottom of sign.
48 Tarlow Drive
07 392 4718

```html
<!DOCTYPE html>
<html lang="en">
<head>
<meta charset="utf-8">
<title>Fastlane – Workshop Sign</title>
<link rel="stylesheet" href="https://fonts.googleapis.com/css2?family=Archivo+Black&family=Anton&family=Oswald:wght@300&display=swap">
<style>
  :root {
    --page-grey: #2c2e31;
    --sign-black: #050505;
    --sign-charcoal: #1c1c1c;
    --brand-red: #e21d25;
    --deep-red: #b8141b;
    --silver: #c9c9c9;
    --white: #ffffff;
  }
  * { margin: 0; padding: 0; box-sizing: border-box; }
  html, body {
    width: 915px; height: 1200px; overflow: hidden;
    background: var(--page-grey);
  }
  .sign {
    position: absolute; left: 30px; top: 172px;
    width: 855px; height: 855px;
    background: radial-gradient(ellipse at 55% 45%, var(--sign-charcoal) 0%, var(--sign-black) 70%);
    overflow: hidden;
  }
  .sign-graphics { position: absolute; inset: 0; }
  .brand-name {
    position: absolute; top: 52px; left: 0; width: 100%;
    text-align: center;
    font-family: "Archivo Black", sans-serif;
    font-size: 72px; letter-spacing: 4px; line-height: 1;
    color: var(--brand-red);
    text-transform: uppercase;
  }
  .service-label {
    position: absolute; width: 170px; transform: translateX(-50%);
    text-align: center;
    font-family: "Archivo Black", sans-serif;
    font-size: 16.5px; line-height: 1.25; letter-spacing: 0.4px;
    color: var(--white); text-transform: uppercase;
  }
  .contact-phone {
    position: absolute; top: 652px; left: 210px;
    display: flex; align-items: center; gap: 22px;
  }
  .phone-number {
    font-family: "Anton", sans-serif;
    font-size: 66px; line-height: 1; letter-spacing: 2px;
    color: var(--white);
  }
  .contact-address {
    position: absolute; top: 742px; left: 0; width: 100%;
    text-align: center;
    font-family: "Oswald", sans-serif; font-weight: 300;
    font-size: 28px; color: var(--white);
  }
</style>
</head>
<body>
<main class="sign">
  <svg class="sign-graphics" width="855" height="855" viewBox="0 0 855 855">
    <defs>
      <linearGradient id="silver-rim" x1="0" y1="0" x2="1" y2="1">
        <stop offset="0" stop-color="#f2f2f2"/>
        <stop offset="0.5" stop-color="#9a9a9a"/>
        <stop offset="1" stop-color="#e0e0e0"/>
      </linearGradient>
      <linearGradient id="red-face" x1="0" y1="0" x2="1" y2="1">
        <stop offset="0" stop-color="#e8242c"/>
        <stop offset="1" stop-color="#b8141b"/>
      </linearGradient>
      <polygon id="hex-rim" points="0,-67 58,-33.5 58,33.5 0,67 -58,33.5 -58,-33.5"/>
      <polygon id="hex-face" points="0,-59 51,-29.5 51,29.5 0,59 -51,29.5 -51,-29.5"/>
    </defs>

    <rect class="track-texture" role="img" aria-label="Faint tyre-track texture across the sign" x="0" y="280" width="855" height="260" fill="#161616" opacity="0.7"/>

    <g class="hex-connectors" stroke="#e21d25" stroke-width="2" stroke-dasharray="2 3">
      <line x1="185" y1="402" x2="212" y2="428"/><line x1="193" y1="396" x2="220" y2="422"/>
      <line x1="300" y1="402" x2="273" y2="428"/><line x1="292" y1="396" x2="265" y2="422"/>
      <line x1="352" y1="402" x2="380" y2="428"/><line x1="360" y1="396" x2="388" y2="422"/>
      <line x1="467" y1="402" x2="440" y2="428"/><line x1="459" y1="396" x2="432" y2="422"/>
      <line x1="520" y1="402" x2="552" y2="428"/><line x1="528" y1="396" x2="560" y2="422"/>
      <line x1="635" y1="402" x2="612" y2="428"/><line x1="627" y1="396" x2="604" y2="422"/>
    </g>

    <g class="service-hexes">
      <g transform="translate(158 345)" role="img" aria-label="Warrant of fitness icon: document with shield and tick"><use href="#hex-rim" fill="url(#silver-rim)"/><use href="#hex-face" fill="url(#red-face)"/></g>
      <g transform="translate(326 340)" role="img" aria-label="Vehicle servicing icon: car front"><use href="#hex-rim" fill="url(#silver-rim)"/><use href="#hex-face" fill="url(#red-face)"/></g>
      <g transform="translate(493 337)" role="img" aria-label="Mechanical repairs icon: hand holding spanner"><use href="#hex-rim" fill="url(#silver-rim)"/><use href="#hex-face" fill="url(#red-face)"/></g>
      <g transform="translate(661 333)" role="img" aria-label="Tyres and wheel alignment icon: wheel"><use href="#hex-rim" fill="url(#silver-rim)"/><use href="#hex-face" fill="url(#red-face)"/></g>
      <g transform="translate(242 467)" role="img" aria-label="Batteries and diagnostics icon: car battery"><use href="#hex-rim" fill="url(#silver-rim)"/><use href="#hex-face" fill="url(#red-face)"/></g>
      <g transform="translate(417 462)" role="img" aria-label="Automotive parts icon: engine and gear"><use href="#hex-rim" fill="url(#silver-rim)"/><use href="#hex-face" fill="url(#red-face)"/></g>
      <g transform="translate(590 458)" role="img" aria-label="Vehicle sales icon: car side view"><use href="#hex-rim" fill="url(#silver-rim)"/><use href="#hex-face" fill="url(#red-face)"/></g>
    </g>

    <g class="corner-bands">
      <polygon points="0,812 200,812 230,855 0,855" fill="#e21d25"/>
      <polyline points="0,800 198,800 236,855" fill="none" stroke="#ffffff" stroke-width="2"/>
      <polygon points="855,794 650,794 620,855 855,855" fill="#e21d25"/>
      <polyline points="855,782 652,782 616,855" fill="none" stroke="#ffffff" stroke-width="2"/>
    </g>
  </svg>

  <h1 class="brand-name">Fastlane</h1>

  <p class="service-label" style="left:158px; top:208px;">Warrant<br>of Fitness</p>
  <p class="service-label" style="left:326px; top:204px;">Vehicle<br>Servicing</p>
  <p class="service-label" style="left:493px; top:194px;">All<br>Mechanical<br>Repairs</p>
  <p class="service-label" style="left:661px; top:192px;">Tyres &amp;<br>Wheel<br>Alignments</p>
  <p class="service-label" style="left:239px; top:572px;">Batteries &amp;<br>Diagnostics</p>
  <p class="service-label" style="left:432px; top:566px;">Automotive<br>Parts</p>
  <p class="service-label" style="left:597px; top:563px;">Vehicle<br>Sales.</p>

  <div class="contact-phone">
    <svg class="phone-icon" width="54" height="54" viewBox="0 0 54 54" aria-hidden="true">
      <circle cx="27" cy="27" r="27" fill="#e21d25"/>
      <path d="M19 14c2-1 4 0 5 2l2 5c1 2 0 3-1 4l-2 1c1 4 4 7 8 9l1-2c1-1 2-2 4-1l5 2c2 1 3 3 2 5l-1 2c-1 2-4 3-7 2-9-3-16-10-19-19-1-3 0-6 3-7z" fill="#050505"/>
    </svg>
    <span class="phone-number">07 392 4718</span>
  </div>
  <p class="contact-address">48 Tarlow Drive</p>
</main>
</body>
</html>
```